Nature and Scenic Photographs Business Card Design

I require a simple business card using the illustration that I have provided

Industry/Entity Type

Business

Contact Information for Business Card

Gil Harlow
Mobile: 0436182057
Skype: gilbert.moray.harlow

```html
<!DOCTYPE html>
<html lang="en">
<head>
<meta charset="utf-8">
<title>Gil Harlow Photography – Business Card</title>
<link rel="stylesheet" href="https://fonts.googleapis.com/css2?family=PT+Sans:wght@400&display=swap">
<style>
  :root {
    --backdrop: #343d3f;
    --card-black: #050505;
    --forest-deep: #1f2a14;
    --forest-mid: #3f5a22;
    --forest-light: #7c9a3e;
    --leaf-litter: #5a4128;
    --band-brown: rgba(38, 22, 16, 0.88);
    --brand-green: #6f9a3a;
  }
  html, body {
    margin: 0;
    padding: 0;
    width: 1200px;
    height: 1122px;
    overflow: hidden;
    background: var(--backdrop);
  }
  .business-card {
    position: absolute;
    left: 140px;
    top: 281px;
    width: 920px;
    height: 560px;
    font-family: "PT Sans", sans-serif;
    color: var(--brand-green);
  }
  .card-art {
    position: absolute;
    inset: 0;
  }
  .brand-name {
    position: absolute;
    left: 74px;
    top: 368px;
    margin: 0;
    font-size: 50px;
    font-weight: 400;
    line-height: 1;
    letter-spacing: -0.5px;
  }
  .brand-tagline {
    position: absolute;
    left: 76px;
    top: 424px;
    margin: 0;
    font-size: 25px;
    font-weight: 400;
    line-height: 1;
    text-transform: uppercase;
  }
  .contact-list {
    position: absolute;
    left: 604px;
    top: 418px;
    margin: 0;
    padding: 0;
    list-style: none;
    font-size: 18px;
    line-height: 1;
  }
  .contact-item {
    display: flex;
    align-items: center;
    gap: 8px;
    height: 28px;
  }
  .contact-icon {
    width: 20px;
    height: 20px;
    flex: none;
  }
</style>
</head>
<body>
  <article class="business-card">
    <svg class="card-art" width="920" height="560" viewBox="0 0 920 560" aria-hidden="false">
      <defs>
        <linearGradient id="forestTones" x1="0" y1="0" x2="1" y2="1">
          <stop offset="0" stop-color="var(--forest-deep)"/>
          <stop offset="0.35" stop-color="var(--forest-mid)"/>
          <stop offset="0.6" stop-color="var(--forest-light)"/>
          <stop offset="1" stop-color="var(--leaf-litter)"/>
        </linearGradient>
      </defs>
      <rect class="card-base" x="0" y="0" width="920" height="560" fill="var(--card-black)"/>
      <path class="photo-window" role="img" aria-label="Photograph of a mossy rainforest floor with fallen branches, ferns and tree trunks"
        fill="url(#forestTones)"
        d="M38 36 H428 L440 48 L452 36 H882 V430 L872 442 L882 454 V524 H440 L428 512 L416 524 H38 V212 L48 200 L38 188 Z"/>
      <path class="name-band" fill="var(--band-brown)"
        d="M38 350 H540 L560 390 H882 V430 L872 442 L882 454 V524 H440 L428 512 L416 524 H38 Z"/>
    </svg>

    <h1 class="brand-name">Gil Harlow</h1>
    <p class="brand-tagline">Photography</p>

    <ul class="contact-list">
      <li class="contact-item">
        <svg class="contact-icon" viewBox="0 0 20 20"><rect x="2" y="5" width="16" height="11" fill="var(--brand-green)"/><path d="M2 5 L10 11 L18 5" fill="none" stroke="#241510" stroke-width="1.4"/></svg>
        <span>gil.har3@mailbox</span>
      </li>
      <li class="contact-item">
        <svg class="contact-icon" viewBox="0 0 20 20"><rect x="6" y="2" width="9" height="16" rx="1.5" fill="var(--brand-green)"/><rect x="8" y="4.5" width="5" height="5" fill="#241510"/></svg>
        <span>0436182057</span>
      </li>
      <li class="contact-item">
        <svg class="contact-icon" viewBox="0 0 20 20"><circle cx="10" cy="10" r="9" fill="var(--brand-green)"/></svg>
        <span>gilbert.moray.harlow</span>
      </li>
    </ul>
  </article>
</body>
</html>
```